Flyer/Broschürre für Ambulanter Betreuungsdienst
Zielgruppe
Ambulanter Betreuungsdienst,Dienstleistungen für Senioren und Menschen mit Beeinträchtigung
Nach Paragraph 43b 45a/b & 53b SGBXI
Unterstützung im Alltag:
-Begleitung zu Arztbesuchen,Therapien &Terminbegleitung aller Art,
-Hilfe beim Einkaufen & Besorgungen + Transport
-Unterstützung bei der Tagesstrukturierung & Organisation im Alltag
-Erinnerungsservice zb. Einahme von Medikamenten ggbf. Kontrolle
-Begleitung zu Sportveranstaltungen,Theater uvm.
für zuverlässige Sicherheit und Orientierung.
-Gemeinsames Spazieren gehen ( Bewegungsangebote)
- Lesen & Vorlesen
-Gemeinsames Kochen und geselschaft leisten beim essen.
-Unterstützung bei Terminplanungen,Hilfe bei der komunikation mit Medizinischen Personal.
Soziale Betreuung & Aktivierung:
-Geselschaft leisten,Gespräche führen ;
-Freizeitaktivitäten Planen & Durchführen
-Gemeinsames Lesen und Vorlesen
-Karten & Brettspiele spielen
-Malen & Basteln
-Briefe schreiben,Emails verfassen
-Gemeinsam alte interessen wecken und neue finden.
-Angehörige entlasten
-kommunikation & Informationsaustausch über Fortschritte und Bedürfnisse
-Betreuung & Aktivierung für Menschen mit Demenz
-Erinnerungspflege,Biografie Arbeit
-Individuelle Betreuung
-Kurz und Langzeit Betreuung
-Nachtpflege
-Bewegungsangebote
-Spiele spielen zb. Brett & Gemeinschsftsspiele
Dienstleistungen Haushaltsbereich
-Reinigung von Böden(Saugen & Wischen)
-Reinigung Küche und Bad
-Bett frisch Beziehen
-Fenster Reinigung (innen & außen)
-Haustiere versorgen (mit dem Hund spazieren gehen)
-Wäsche waschen
-Dekorieren
-uvm
Aufgabenstellung
Freundliches Design , vertrauenswürdiges Erscheinungsbild mit warmen Farben.
Firmenname ( Sonnwerk) logo sollte einen Sonnwerk darstellen.
Slogan Text:
Verlässlichkeit und Fürsorge mit Herz & Verstand.
Format soll handlich und nicht zu klein sein,damit Senioren es gut lesen bzw erkennen können.

```html
<!DOCTYPE html>
<html lang="de">
<head>
<meta charset="utf-8">
<title>Sonnwerk – Flyer Ambulanter Betreuungsdienst</title>
<link href="https://fonts.googleapis.com/css2?family=Merriweather+Sans:wght@400;700;800&family=Roboto+Condensed:wght@300;400&family=Dancing+Script:wght@500&display=swap" rel="stylesheet">
<style>
  :root {
    --teal: #21b3b2;
    --teal-dark: #1a9e9d;
    --orange: #ec7a45;
    --sticker: #c6552a;
    --white: #ffffff;
    --ink: #161616;
    --stage: #d9d9d9;
    --body: "Merriweather Sans", sans-serif;
    --head: "Roboto Condensed", sans-serif;
    --script: "Dancing Script", cursive;
  }
  * { box-sizing: border-box; margin: 0; padding: 0; }
  html, body { width: 1200px; height: 1163px; overflow: hidden; }
  body { background: var(--stage); position: relative; font-family: var(--body); color: var(--white); }

  .brand { font-family: var(--body); font-weight: 800; color: var(--ink); display: inline-flex; align-items: center; gap: 6px; letter-spacing: .2px; }
  .brand .dot { width: .55em; height: .55em; border-radius: 50%; background: var(--teal); display: inline-block; }

  .photo { position: absolute; }

  /* Front cover */
  .cover { position: absolute; left: 84px; top: 138px; width: 338px; height: 486px; background: var(--teal); overflow: hidden; box-shadow: 0 2px 6px rgba(0,0,0,.25); }
  .cover-head { position: absolute; left: 0; top: 0; width: 100%; height: 95px; background: var(--white); display: flex; align-items: center; justify-content: center; }
  .cover-head .brand { font-size: 30px; }
  .cover-photo { left: 0; top: 95px; width: 338px; height: 205px; clip-path: polygon(0 0, 100% 0, 100% 100%, 62px 100%, 0 9%);
    background: radial-gradient(circle at 30% 25%, #fff4d6 0, #f2c27a 14%, transparent 34%), linear-gradient(120deg, #6b4a2f 0%, #b6724b 35%, #4f6b3a 60%, #2f3a24 100%); }
  .cover-text { position: absolute; left: 0; top: 312px; width: 100%; text-align: center; }
  .slogan { font-family: var(--script); font-size: 20px; line-height: 1.05; font-weight: 500; }
  .cover-lead { margin-top: 16px; font-size: 11.3px; line-height: 1.25; }
  .cover-lead b { font-weight: 800; }
  .cover-lead + .cover-lead { margin-top: 7px; }

  /* Inner spread */
  .spread { position: absolute; left: 81px; top: 641px; width: 687px; height: 490px; box-shadow: 0 2px 6px rgba(0,0,0,.25); }
  .panel-alltag { position: absolute; left: 0; top: 0; width: 206px; height: 490px; background: var(--teal); }
  .panel-title { font-family: var(--head); font-weight: 300; font-size: 18.5px; line-height: 1.2; }
  .panel-alltag .panel-title { position: absolute; left: 29px; top: 22px; }
  .list { list-style: none; font-size: 9px; line-height: 1.18; }
  .list li { position: relative; padding-left: 9px; margin-bottom: 4.6px; }
  .list li::before { content: ""; position: absolute; left: 0; top: 4px; width: 2.4px; height: 2.4px; background: currentColor; border-radius: 50%; opacity: .9; }
  .panel-alltag .list { position: absolute; left: 29px; top: 74px; width: 166px; }
  .quote-box { position: absolute; left: 0; top: 357px; width: 206px; height: 133px; background: var(--orange); padding: 9px 4px 0 30px; }
  .quote-box p { font-size: 10px; line-height: 1.28; }
  .phone-line { display: flex; align-items: center; gap: 9px; margin-top: 9px; font-size: 13.5px; letter-spacing: .5px; }
  .phone-line svg { width: 11px; height: 14px; }

  .photo-strip { position: absolute; left: 206px; top: 0; width: 137px; height: 490px; }
  .photo-walk { left: 0; top: 0; width: 137px; height: 229px; background: linear-gradient(160deg, #cfe7b4 0%, #7ea85a 45%, #4d7a38 100%); }
  .photo-laugh { left: 0; top: 229px; width: 137px; height: 128px; background: linear-gradient(160deg, #e9e7e2 0%, #c7b9ad 50%, #9c3b32 100%); }
  .photo-puzzle { left: 0; top: 357px; width: 137px; height: 133px; background: linear-gradient(160deg, #d9b7b9 0%, #c99d8a 50%, #d8a86a 100%); }

  .panel-care { position: absolute; left: 343px; top: 0; width: 344px; height: 490px; background: var(--teal); overflow: hidden; }
  .photo-kitchen { left: 0; top: 0; width: 344px; height: 228px; clip-path: polygon(0 0, 100% 0, 100% 0, 271px 100%, 0 100%);
    background: linear-gradient(170deg, #efece6 0%, #d8cfc5 45%, #b94a3a 70%, #f2eee8 100%); }
  .brand-band { position: absolute; left: 90px; top: 180px; width: 200px; height: 48px; background: var(--white); clip-path: polygon(0 0, 100% 0, 91% 100%, 0 100%); display: flex; align-items: center; padding-left: 16px; }
  .brand-band .brand { font-size: 23px; }
  .care-col { position: absolute; top: 239px; }
  .care-col.demenz { left: 14px; width: 128px; }
  .care-col.sozial { left: 162px; width: 164px; }
  .care-col.demenz .list { margin-top: 30px; }
  .care-col.sozial .list { margin-top: 10px; }

  .panel-back { position: absolute; left: 784px; top: 641px; width: 341px; height: 490px; background: var(--teal); overflow: hidden; box-shadow: 0 2px 6px rgba(0,0,0,.25); }
  .back-white { position: absolute; left: 0; top: 277px; width: 341px; height: 213px; background: var(--white); clip-path: polygon(0 0, 278px 0, 341px 197px, 341px 100%, 0 100%); }
  .panel-back .panel-title { position: absolute; left: 40px; top: 38px; }
  .panel-back .list { position: absolute; left: 40px; top: 96px; width: 290px; font-size: 9.2px; }
  .panel-back .list li { margin-bottom: 5.4px; }
  .sticker { position: absolute; left: 73px; top: 215px; width: 104px; height: 104px; border-radius: 50%; background: var(--sticker); display: flex; align-items: center; justify-content: center; text-align: center; transform: rotate(-17deg); box-shadow: 0 2px 4px rgba(0,0,0,.25); }
  .sticker p { font-size: 6.8px; line-height: 1.3; font-weight: 700; width: 80px; }
  .back-brand { position: absolute; left: 89px; top: 330px; }
  .back-brand .brand { font-size: 25px; }
  .contact { position: absolute; left: 88px; top: 378px; list-style: none; color: var(--teal-dark); }
  .contact li { display: flex; align-items: center; gap: 8px; font-size: 9.5px; height: 22px; }
  .contact li.big { font-size: 13px; letter-spacing: .5px; }
  .contact svg { width: 11px; height: 11px; fill: var(--teal-dark); }
</style>
</head>
<body>

<section class="cover">
  <div class="cover-head"><span class="brand">Sonnwerk<span class="dot"></span></span></div>
  <div class="photo cover-photo" role="img" aria-label="Foto: Hände halten sich im Gegenlicht, Frau im Rollstuhl"></div>
  <div class="cover-text">
    <p class="slogan">„Verlässlichkeit und Fürsorge<br>mit Herz &amp; Verstand“</p>
    <p class="cover-lead"><b>Wir unterstützen Senioren und Menschen mit<br>Beeinträchtigung im Alltag –</b><br>zuverlässig, herzlich und individuell.</p>
    <p class="cover-lead">Ob Begleitung, Haushalt oder soziale Betreuung:<br><b>Sonnwerk</b> schafft Orientierung,<br>Entlastung und mehr Lebensqualität.</p>
  </div>
</section>

<section class="spread">
  <div class="panel-alltag">
    <h2 class="panel-title">Unterstützung<br>im Alltag</h2>
    <ul class="list">
      <li>Begleitung zu Arztbesuchen, Therapien und Terminbeglei­tungen aller Art</li>
      <li>Hilfe beim Einkaufen und bei Besorgungen + Transport</li>
      <li>Unterstützung bei der Tagesstrukturierung und Organisation im Alltag</li>
      <li>Erinnerungsservice, z. B. Einnahme von Medikamenten, ggf. Kontrolle</li>
      <li>Begleitung zu Sportveran­staltungen, Theater u. v. m. für zuverlässige Sicherheit und Orientierung</li>
      <li>Gemeinsame Spaziergänge (Bewegungsangebote)</li>
      <li>Lesen und Vorlesen</li>
      <li>Gemeinsames Kochen und Gesellschaft leisten beim Essen</li>
      <li>Unterstützung bei Terminplanungen, Hilfe bei der Kommunikation mit medizinischem Personal</li>
    </ul>
    <div class="quote-box">
      <p>„Gerne stehe ich Ihnen für ein Beratungsgespräch zur Verfügung, damit wir gemeinsam Wege finden, Ihren Alltag zu erleichtern und Ihren Angehörigen bestmöglich zu begleiten.“</p>
      <div class="phone-line">
        <svg viewBox="0 0 11 14" fill="none" stroke="#fff" stroke-width="1.2"><rect x="1" y="1" width="7" height="12" rx="1.5"/><path d="M9 5 q1.5 2 0 4"/></svg>
        <span>+49 30 98 76 54 32</span>
      </div>
    </div>
  </div>

  <div class="photo-strip">
    <div class="photo photo-walk" role="img" aria-label="Foto: Betreuerin begleitet Seniorin im Rollstuhl im Grünen"></div>
    <div class="photo photo-laugh" role="img" aria-label="Foto: lachender Senior im Rollstuhl mit Hund"></div>
    <div class="photo photo-puzzle" role="img" aria-label="Foto: Hände legen bunte Holzformen in ein Legespiel"></div>
  </div>

  <div class="panel-care">
    <div class="photo photo-kitchen" role="img" aria-label="Foto: zwei Frauen schneiden gemeinsam Obst in der Küche"></div>
    <div class="brand-band"><span class="brand">Sonnwerk<span class="dot"></span></span></div>
    <div class="care-col demenz">
      <h2 class="panel-title">Betreuung &amp;<br>Aktivierung für<br>Menschen mit<br>Demenz</h2>
      <ul class="list">
        <li>Erinnerungspflege, Biografiearbeit</li>
        <li>Individuelle Betreuung</li>
        <li>Kurz- und Langzeitbetreuung</li>
        <li>Nachtpflege</li>
        <li>Bewegungsangebote</li>
        <li>Spiele spielen, z. B. Brett- und Gemeinschaftsspiele</li>
      </ul>
    </div>
    <div class="care-col sozial">
      <h2 class="panel-title">Soziale Betreuung<br>&amp; Aktivierung</h2>
      <ul class="list">
        <li>Gesellschaft leisten, Gespräche führen</li>
        <li>Freizeitaktivitäten planen und durchführen</li>
        <li>Gemeinsames Lesen und Vorlesen</li>
        <li>Karten- und Brettspiele spielen</li>
        <li>Malen und Basteln</li>
        <li>Briefe schreiben, E-Mails verfassen</li>
        <li>Gemeinsam alte Interessen wecken und neue finden</li>
        <li>Angehörige entlasten</li>
        <li>Kommunikation und Informationsaustausch über Fortschritte und Bedürfnisse</li>
      </ul>
    </div>
  </div>
</section>

<section class="panel-back">
  <div class="back-white"></div>
  <h2 class="panel-title">Dienstleistungen im<br>Haushaltsbereich</h2>
  <ul class="list">
    <li>Reinigung von Böden (Saugen und Wischen)</li>
    <li>Reinigung von Küche und Bad</li>
    <li>Bett frisch beziehen</li>
    <li>Fensterreinigung (innen und außen)</li>
    <li>Haustiere versorgen<br>(mit dem Hund spazieren gehen)</li>
    <li>Wäsche waschen</li>
    <li>Dekorieren</li>
    <li>u. v. m.</li>
  </ul>
  <div class="sticker"><p>Ambulanter Betreuungs­dienst, Dienstleistungen für Senioren und Menschen mit Beeinträchtigung Nach Paragraph 43b 45a/b &amp; 53b SGBXI</p></div>
  <div class="back-brand"><span class="brand">Sonnwerk<span class="dot"></span></span></div>
  <ul class="contact">
    <li><svg viewBox="0 0 11 11"><path d="M5.5 0a3.8 3.8 0 0 0-3.8 3.8C1.7 6.6 5.5 11 5.5 11s3.8-4.4 3.8-7.2A3.8 3.8 0 0 0 5.5 0zm0 5.3a1.5 1.5 0 1 1 0-3 1.5 1.5 0 0 1 0 3z"/></svg>Lindenweg 8, 54321 Lindenfeld</li>
    <li class="big"><svg viewBox="0 0 11 11" fill="none" stroke="#1a9e9d" stroke-width="1"><rect x="2" y=".5" width="5.5" height="10" rx="1"/><path d="M8.5 3.5q1.2 2 0 4"/></svg>+49 30 98 76 54 32</li>
    <li><svg viewBox="0 0 11 11"><path d="M0 2h11v7H0z"/><path d="M0 2l5.5 4L11 2" fill="none" stroke="#fff" stroke-width=".9"/></svg>info@sonnwerk.de</li>
    <li><svg viewBox="0 0 11 11"><circle cx="5.5" cy="5.5" r="5"/><path d="M.5 5.5h10M5.5.5c-2.5 3-2.5 7 0 10M5.5.5c2.5 3 2.5 7 0 10" fill="none" stroke="#fff" stroke-width=".7"/></svg>www.sonnwerk.de</li>
  </ul>
</section>

</body>
</html>
```